Varemo Group Business Card Design

The CEO is looking for a new trendy look for his business card.
You can stay with current branding or come up with something new/creative. It can be 3D, including Medical Office buildings. You can use our logo in a variety of colors. Please include name, title, company name, company website, email address, cell number

Target Market(s)

Real Estate Development and Construction

Industry/Entity Type

Health care real estate

Contact Information for Business Card

Rohesh Kumbar, CEO M-727.418.9062 E-roheshkumbar@varemo.com Address:4100 Lindell Ave, Tampa, FL 33611 www.varemo.com

Font styles to use
Other font styles liked:
• Be creative

Requirements
Must have
• Creative, trendy look
Nice to have
• Please go to our website to get a feel- www. varemo.com
Should not have
• small fonts

```html
<!DOCTYPE html>
<html lang="en">
<head>
<meta charset="utf-8">
<title>Varemo Group – Business Card</title>
<link rel="stylesheet" href="https://fonts.googleapis.com/css2?family=Poppins:wght@300;400;600;800&display=swap">
<style>
  :root{
    --brand-red:#b41e2b;
    --brand-red-deep:#9e1824;
    --navy:#1d2b50;
    --grey:#6b6f76;
    --paper:#ffffff;
    --stage:#e4e5e7;
    --sketch-light:#eef0f2;
  }
  *{box-sizing:border-box;margin:0;padding:0}
  html,body{width:1200px;height:952px;overflow:hidden}
  body{background:var(--stage);font-family:"Poppins",sans-serif;position:relative}
  .card{position:absolute;left:240px;width:720px;height:411px;overflow:hidden;box-shadow:0 6px 18px rgba(0,0,0,.18)}
  .card--front{top:45px;background:var(--paper)}
  .card--back{top:496px;background:var(--brand-red)}

  .sketch-area{position:absolute}
  .card--front .sketch-area{left:170px;top:170px;width:550px;height:241px;
    background:linear-gradient(135deg,rgba(238,240,242,0) 0%,var(--sketch-light) 45%,#e6e8eb 100%)}
  .card--back .sketch-area{left:60px;top:40px;width:600px;height:340px;
    background:radial-gradient(ellipse at center,rgba(158,24,36,.55) 0%,rgba(158,24,36,0) 70%)}

  .wordmark{position:absolute;font-weight:800;line-height:1;letter-spacing:-1px}
  .card--front .wordmark{left:150px;top:46px;font-size:44px;color:var(--brand-red)}
  .card--back .wordmark{left:0;right:0;top:170px;text-align:center;font-size:62px;color:var(--paper)}

  .contact-list{position:absolute;left:40px;top:140px;list-style:none}
  .contact-list li{display:flex;align-items:flex-start;gap:10px;font-size:13px;color:var(--grey);margin-bottom:10px;line-height:1.35}
  .contact-list svg{flex:none;width:18px;height:18px;margin-top:1px}

  .identity{position:absolute;right:80px;top:236px;text-align:right}
  .identity__name{font-size:26px;letter-spacing:1.5px;color:var(--navy);font-weight:400}
  .identity__name strong{color:var(--brand-red);font-weight:600}
  .identity__title{font-size:15px;color:var(--grey);letter-spacing:1px;margin-top:2px}
  .accent-block{position:absolute;right:0;top:246px;width:58px;height:46px;background:var(--brand-red)}
</style>
</head>
<body>

<section class="card card--front" aria-label="Card front">
  <div class="sketch-area" role="img" aria-label="Faint architectural sketch of a medical office building"></div>
  <div class="wordmark">Varemo Group</div>

  <ul class="contact-list">
    <li>
      <svg viewBox="0 0 18 18"><rect width="18" height="18" rx="3" fill="#b41e2b"/><path d="M9 3.5a3.5 3.5 0 0 0-3.5 3.5c0 2.6 3.5 7 3.5 7s3.5-4.4 3.5-7A3.5 3.5 0 0 0 9 3.5z" fill="#fff"/><circle cx="9" cy="7" r="1.3" fill="#b41e2b"/></svg>
      <span>4100 Lindell Ave, Tampa<br>FL 33611</span>
    </li>
    <li>
      <svg viewBox="0 0 18 18"><rect width="18" height="18" rx="3" fill="#1d2b50"/><path d="M6 4l2 2.5-1.2 1.3a7 7 0 0 0 3.4 3.4L11.5 10 14 12l-1 2c-4.5-.3-8.7-4.5-9-9z" fill="#fff"/></svg>
      <span>727.418.9062</span>
    </li>
    <li>
      <svg viewBox="0 0 18 18"><rect width="18" height="18" rx="3" fill="#1d2b50"/><rect x="4" y="5.5" width="10" height="7" fill="none" stroke="#fff" stroke-width="1.2"/><path d="M4 5.5l5 4 5-4" fill="none" stroke="#fff" stroke-width="1.2"/></svg>
      <span>roheshkumbar@varemo.com</span>
    </li>
    <li>
      <svg viewBox="0 0 18 18"><rect width="18" height="18" rx="3" fill="#1d2b50"/><path d="M6 4l7 5-3 .8 1.8 3.4-1.4.7-1.8-3.4L6 12.5z" fill="#fff"/></svg>
      <span>www.varemo.com</span>
    </li>
  </ul>

  <div class="identity">
    <div class="identity__name">ROHESH <strong>KUMBAR</strong></div>
    <div class="identity__title">CEO</div>
  </div>
  <div class="accent-block"></div>
</section>

<section class="card card--back" aria-label="Card back">
  <div class="sketch-area" role="img" aria-label="Faint architectural sketch of a medical office building in red tones"></div>
  <div class="wordmark">Varemo Group</div>
</section>

</body>
</html>
```